tall cedar health and wellness group.

need a full website design , all information provided in word document labeled website blue print
Updates

Need extra days to review

Target Market(s)

first responders, military , people in crisis

Coding

Coded - Design and coding required

Number of Pages Required

1 page

```html
<!DOCTYPE html>
<html lang="en">
<head>
<meta charset="utf-8">
<title>Tall Cedar Health &amp; Wellness Group</title>
<link rel="stylesheet" href="https://fonts.googleapis.com/css2?family=Jost:wght@400;500&family=Playfair+Display:wght@400&display=swap">
<style>
:root{
  --ink:#0b0b0b;
  --white:#ffffff;
  --cyan:#13c3ef;
  --cyan-soft:#22c6ef;
  --blue:#2b5c9c;
  --text-dark:#1d1d1d;
  --muted:#cfd6de;
}
*{margin:0;padding:0;box-sizing:border-box}
html,body{width:1200px;height:3172px;overflow:hidden;background:var(--white)}
body{position:relative;font-family:'Jost',sans-serif;color:var(--text-dark)}
.abs{position:absolute}
.serif{font-family:'Playfair Display',serif;font-weight:400}
.btn{position:absolute;display:flex;align-items:center;justify-content:center;border-radius:20px;font-size:13px;font-family:'Jost',sans-serif}
.btn-cyan{background:var(--cyan);color:var(--white)}
.btn-white{background:var(--white);color:var(--text-dark)}
.photo{position:absolute}

/* header */
.site-header{left:0;top:0;width:1200px;height:79px;background:var(--ink)}
.brand{left:146px;top:10px;width:110px;text-align:center;color:#3a78c9}
.brand-mark{display:block;margin:0 auto 3px;width:26px;height:26px;border:2px solid #8d96a3}
.brand-name{font-size:14px;font-weight:500;letter-spacing:.5px;line-height:1}
.brand-sub{font-size:6px;color:#9aa3ad;letter-spacing:.3px;margin-top:2px}
.main-nav{top:30px;left:0;width:1200px;height:20px}
.main-nav a{position:absolute;color:var(--white);text-decoration:none;font-size:13px;transform:translateX(-50%)}

/* hero */
.hero{left:0;top:79px;width:1200px;height:574px;background:linear-gradient(180deg,#5c5346 0%,#3b342c 45%,#1c1916 100%)}
.hero-band{left:0;top:631px;width:1200px;height:22px;background:#1a1a1a}
.hero-title{left:0;top:295px;width:1200px;text-align:center;color:var(--white);font-size:54px;line-height:58px}
.hero-lead{left:380px;top:428px;width:440px;text-align:center;color:var(--white);font-size:13px;line-height:17px}
.arrow{position:absolute}

/* about */
.about{left:0;top:653px;width:1200px;height:569px;background:var(--blue)}
.section-title{position:absolute;font-size:44px;line-height:1.1}
.body-text{position:absolute;font-size:13px;line-height:17px}
.body-text p+p{margin-top:17px}

/* services */
.services-bg{left:0;top:1673px;width:1200px;height:387px;background:linear-gradient(180deg,#1d1d1d,#0d0d0d)}
.service-card{position:absolute}
.service-label{position:absolute;left:0;bottom:22px;width:100%;text-align:center;color:var(--white);font-size:18px}

/* mission */
.mission{left:600px;top:2402px;width:600px;height:364px;background:var(--cyan-soft)}

/* partners */
.partner{position:absolute;top:2828px;font-size:17px;font-weight:500;display:flex;align-items:center;gap:7px;transform:translateX(-50%);white-space:nowrap}
.partner i{display:inline-block;width:18px;height:18px;background:currentColor}

/* footer */
.site-footer{left:0;top:2910px;width:1200px;height:262px;background:var(--ink)}
.footer-nav a{position:absolute;top:3091px;color:var(--white);text-decoration:none;font-size:13px;transform:translateX(-50%)}
.social{position:absolute;top:3043px;width:24px;height:24px;border:1.5px solid var(--white);border-radius:50%}
.rule{left:0;top:3134px;width:1200px;height:1px;background:#4a4a4a}
.copyright{left:0;top:3148px;width:1200px;text-align:center;color:var(--white);font-size:10px}
</style>
</head>
<body>

<header class="abs site-header">
  <div class="abs brand">
    <span class="brand-mark"></span>
    <div class="brand-name">TALL CEDAR</div>
    <div class="brand-sub">HEALTH &amp; WELLNESS GROUP</div>
  </div>
  <nav class="abs main-nav">
    <a style="left:386px">Home</a>
    <a style="left:462px">About Us</a>
    <a style="left:546px">Services</a>
    <a style="left:630px">Our Team</a>
    <a style="left:731px">Join Our Team</a>
    <a style="left:817px">FAQ</a>
  </nav>
  <div class="btn btn-cyan" style="left:922px;top:18px;width:128px;height:39px">Contact</div>
</header>

<section class="abs hero" role="img" aria-label="Counsellor talking with a young couple seated on a sofa in a sunlit office"></section>
<div class="abs hero-band"></div>
<h1 class="abs serif hero-title">Helping Those Who<br>Help Others</h1>
<p class="abs hero-lead">Lorem ipsum dolor sit amet, consectetur adipiscing elit, sed do eiusmod tempor incididunt ut labore et dolore magna aliqua.</p>
<div class="btn btn-cyan" style="left:464px;top:479px;width:129px;height:38px">Contact</div>
<div class="btn btn-white" style="left:607px;top:479px;width:128px;height:38px">Read More</div>
<svg class="arrow" style="left:126px;top:332px" width="62" height="36" viewBox="0 0 62 36" fill="none" stroke="#fff" stroke-width="2.5"><path d="M44 3a15 15 0 1 1 0 30"/><path d="M60 18H4M14 8 4 18l10 10"/></svg>
<svg class="arrow" style="left:1010px;top:332px" width="62" height="36" viewBox="0 0 62 36" fill="none" stroke="#fff" stroke-width="2.5"><path d="M18 3a15 15 0 1 0 0 30"/><path d="M2 18h56M48 8l10 10-10 10"/></svg>

<section class="abs about"></section>
<div class="abs" style="left:149px;top:694px;width:67px;height:64px;background:var(--white)"></div>
<div class="photo" style="left:166px;top:708px;width:340px;height:339px;background:linear-gradient(160deg,#e8e4de,#b9a58e 60%,#6e5646)" role="img" aria-label="Therapist in glasses taking notes in a leather armchair"></div>
<div class="photo" style="left:322px;top:952px;width:269px;height:178px;border:3px solid var(--white);background:linear-gradient(135deg,#9a8a7c,#c9bdb0 50%,#7b6d63)" role="img" aria-label="Video of a counselling session with a client and therapist"></div>
<svg class="abs" style="left:433px;top:1018px" width="50" height="50" viewBox="0 0 50 50" fill="none" stroke="var(--cyan)" stroke-width="2.5"><circle cx="25" cy="25" r="22"/><path d="M20 15l13 10-13 10z"/></svg>
<h2 class="serif section-title" style="left:622px;top:742px;color:var(--white);font-size:54px">About Us</h2>
<div class="body-text" style="left:622px;top:817px;width:430px;color:var(--white)">
  <p>Lorem ipsum dolor sit amet, consectetur adipiscing elit. Pellentesque eget nibh vitae metus viverra ultrices. Ut placerat luctus lorem at malesuada. Phasellus in enim nec turpis efficitur consequat eu at nibh. In eget fermentum ligula, a consectetur dolor.</p>
  <p>Aenean condimentum condimentum vehicula. Lorem ipsum dolor sit amet, consectetur adipiscing elit. Pellentesque eget nibh vitae metus viverra ultrices. Ut placerat luctus lorem at malesuada. Phasellus in enim nec turpis efficitur consequat eu at nibh. In eget fermentum ligula, a consectetur dolor. Aenean condimentum condimentum vehicula.</p>
</div>
<div class="btn btn-white" style="left:622px;top:1030px;width:128px;height:38px">Read more</div>

<div class="abs" style="left:971px;top:1513px;width:96px;height:96px;background:var(--cyan)"></div>
<div class="photo" style="left:695px;top:1172px;width:353px;height:421px;background:linear-gradient(160deg,#1b3d6e,#2c6aa8 45%,#0f2440)" role="img" aria-label="Doctor in a surgical cap reviewing brain scans on monitors"></div>
<h2 class="serif section-title" style="left:150px;top:1300px;color:var(--text-dark)">Who We Serve</h2>
<div class="body-text" style="left:150px;top:1371px;width:470px">
  <p>In ligula lacus, cursus nec consectetur ac, ornare eget nulla. Proin eget purus vitae tellus tempor feugiat non ac nibh. Vivamus sit amet sapien vel velit bibendum sollicitudin congue quis felis. Nullam eu euismod purus. Nulla diam massa, condimentum quis neque ut, consequat efficitur nisi. Quisque in erat eget ipsum tristique consectetur. Nam et luctus orci. Sed varius faucibus auctor.</p>
  <p>Vestibulum ante ipsum primis in faucibus orci luctus et ultrices posuere cubilia curae; Quisque rhoncus non tellus vitae ornare. Donec sit amet dolor fringilla, lobortis lacus ac, facilisis magna.</p>
</div>
<div class="btn btn-cyan" style="left:152px;top:1557px;width:128px;height:38px">Read more</div>

<section class="abs services-bg" role="img" aria-label="Dark background of large leaves"></section>
<h2 class="serif section-title" style="left:0;top:1752px;width:1200px;text-align:center;color:var(--white)">Our Services</h2>
<div class="service-card" style="left:182px;top:1900px;width:236px;height:320px;background:linear-gradient(170deg,#cfc9bf,#8b7f72 55%,#2d2824)" role="img" aria-label="Therapist consoling a distressed client">
  <span class="service-label">Mental Health Therapy</span>
</div>
<div class="service-card" style="left:439px;top:1841px;width:321px;height:438px;background:linear-gradient(170deg,#c9cdd3,#2f4fa0 50%,#1a1d29)" role="img" aria-label="Two paramedics in blue uniforms beside an ambulance">
  <span class="service-label">Trauma &amp; First Responder support</span>
</div>
<div class="service-card" style="left:781px;top:1900px;width:235px;height:320px;background:linear-gradient(170deg,#8a5a2e,#e0a060 45%,#5a3718)" role="img" aria-label="Glowing salt brick wall in a wooden therapy room">
  <span class="service-label">Salt Therapy</span>
</div>
<svg class="arrow" style="left:553px;top:2316px" width="42" height="24" viewBox="0 0 62 36" fill="none" stroke="#111" stroke-width="3"><path d="M44 3a15 15 0 1 1 0 30"/><path d="M60 18H4M14 8 4 18l10 10"/></svg>
<svg class="arrow" style="left:605px;top:2316px" width="42" height="24" viewBox="0 0 62 36" fill="none" stroke="#9a9a9a" stroke-width="3"><path d="M18 3a15 15 0 1 0 0 30"/><path d="M2 18h56M48 8l10 10-10 10"/></svg>

<div class="photo" style="left:0;top:2402px;width:600px;height:364px;background:linear-gradient(160deg,#d8cfc4,#b3a18f 50%,#3f3833)" role="img" aria-label="Counsellor shaking hands with a smiling couple in a living room"></div>
<section class="abs mission"></section>
<h2 class="serif section-title" style="left:617px;top:2462px;color:var(--white)">Mission &amp; Vision</h2>
<div class="body-text" style="left:621px;top:2531px;width:430px;color:var(--white)">
  <p>In ligula lacus, cursus nec consectetur ac, ornare eget nulla. Proin eget purus vitae tellus tempor feugiat non ac nibh. Vivamus sit amet sapien vel velit bibendum sollicitudin congue quis felis. Nullam eu euismod purus. Nulla diam massa, condimentum quis neque ut, consequat.</p>
  <p>Quisque in erat eget ipsum tristique consectetur. Nam et luctus orci. Sed varius faucibus auctor.</p>
</div>
<div class="btn btn-white" style="left:621px;top:2678px;width:128px;height:39px">Read more</div>

<div class="partner" style="left:222px;color:#1f6fd1"><i></i>Northwind</div>
<div class="partner" style="left:379px;color:#1d1d1d">Harbor Ridge</div>
<div class="partner" style="left:515px;color:#2b5c9c">Harbor Ridge</div>
<div class="partner" style="left:644px;color:#1d1d1d">Brightpath</div>
<div class="partner" style="left:813px;color:#1f6fd1"><i></i>Northwind</div>
<div class="partner" style="left:983px;color:#1d1d1d">Harbor Ridge</div>

<footer class="abs site-footer"></footer>
<div class="abs brand" style="left:520px;top:2935px;width:160px">
  <span class="brand-mark" style="width:40px;height:40px;margin-bottom:6px"></span>
  <div class="brand-name" style="font-size:20px">TALL CEDAR</div>
  <div class="brand-sub" style="font-size:8px">HEALTH &amp; WELLNESS GROUP</div>
</div>
<span class="social" style="left:551px" aria-label="Social profile"></span>
<span class="social" style="left:588px" aria-label="Social profile"></span>
<span class="social" style="left:625px" aria-label="Social profile"></span>
<nav class="footer-nav">
  <a style="left:348px">Home</a>
  <a style="left:425px">About Us</a>
  <a style="left:508px">Services</a>
  <a style="left:592px">Our Team</a>
  <a style="left:693px">Join Our Team</a>
  <a style="left:789px">Contact</a>
  <a style="left:856px">FAQ</a>
</nav>
<div class="abs rule"></div>
<p class="abs copyright">Copyright © 2025 tall cedar health and wellness group. All rights reserved.</p>

</body>
</html>
```